DeskWizard.dk Frontpage design

I'm in the process of starting a It-course website, based in Denmark. The web site Url is - www.deskwizard.dk

The services are:
- Online courses (This is the main service and the most important)
- One to One courses
- Webinar

I need a frontpage design a simple design, but it must shows professionalism. I have no preference in color, but I like white space.

In Denmark the established competitors are:
- www.tasniva.dk (Biggest competitor)
- www.bramfeldt.dk/online-kurser
- www.velunda.dk

Target Market(s)

Mainly companies (B to B), but there are also a small number of private customers

Industry/Entity Type

Online it courses and one to one consulting

Number of Pages Required

1 page

Font styles to use
Sans Serif

Requirements
Must have
• A professional design, white space

```html
<!DOCTYPE html>
<html lang="en">
<head>
<meta charset="utf-8">
<title>DeskWizard – Online IT courses</title>
<link href="https://fonts.googleapis.com/css2?family=Outfit:wght@300;400;500;600&display=swap" rel="stylesheet">
<style>
:root{
  --green:#22b24c;
  --green-soft:#e3f5e8;
  --ink:#111417;
  --text:#3b3f44;
  --muted:#80858b;
  --line:#e4e6e8;
  --sand:#f4f3ef;
  --white:#fff;
}
*{box-sizing:border-box;margin:0;padding:0}
html,body{width:1200px;height:4405px;overflow:hidden}
body{font-family:'Outfit',sans-serif;color:var(--text);background:var(--white);font-size:15px;line-height:1.6}
.wrap{width:1030px;margin:0 auto;position:relative}
a{color:inherit;text-decoration:none}
.arrow{display:inline-block;width:14px;height:8px;margin-left:8px;vertical-align:middle}

/* top bar */
.topbar{background:var(--ink);height:41px;color:#fff;font-size:13px}
.topbar .wrap{display:flex;align-items:center;height:41px}
.topbar .item{display:flex;align-items:center;gap:10px;padding-right:20px}
.topbar .sep{width:1px;height:18px;background:#555;margin-right:20px}
.topbar .right{margin-left:auto;display:flex;align-items:center;height:41px}
.topbar .right a{padding:0 18px}
.apply{background:var(--green);height:41px;display:flex;align-items:center;padding:0 20px!important}

/* nav */
.nav{height:74px;border-bottom:1px solid var(--line)}
.nav .wrap{display:flex;align-items:center;height:74px}
.logo{font-size:44px;font-weight:600;color:var(--green);letter-spacing:-.5px;line-height:1}
.menu{margin-left:auto;display:flex;gap:26px;font-size:13.5px;font-weight:500;color:var(--ink);align-items:center}
.menu .bar{width:1px;height:22px;background:#bbb;margin-left:-4px}

/* hero */
.hero{position:relative;height:535px;background:#fff;overflow:hidden}
.hero-photo{position:absolute;left:430px;top:0;right:0;bottom:0;background:linear-gradient(120deg,#f4f4f2 0%,#e9e8e6 45%,#b9a696 70%,#6d5546 100%)}
.hero .wrap{padding-top:92px}
.eyebrow{color:var(--green);font-size:14px;font-weight:500;text-transform:uppercase}
.hero h1{font-size:40px;font-weight:500;color:var(--ink);line-height:1.3;margin-top:6px;width:470px}
.hero p{font-size:15px;width:460px;margin-top:16px;color:var(--ink)}
.actions{display:flex;align-items:center;gap:28px;margin-top:26px}
.btn{display:inline-flex;align-items:center;background:var(--green);color:#fff;font-size:14px;border-radius:4px;height:50px;padding:0 21px}
.watch{display:flex;align-items:center;gap:22px;color:var(--ink);font-size:14px}
.play{width:42px;height:42px;border-radius:50%;background:var(--ink);display:flex;align-items:center;justify-content:center;box-shadow:0 0 0 4px #fff}
.wave{position:absolute;left:0;bottom:0;width:1200px;height:70px}

/* section heads */
.head{text-align:center}
.head h2{font-size:40px;font-weight:500;color:var(--ink);line-height:1.2}
.head h2 span{color:var(--green)}
.underline{display:block;margin:14px auto 0;width:66px;height:10px}

/* why */
.why{padding-top:100px;height:1129px - 650px}
.why .lead{text-align:center;color:var(--ink);font-size:15px;margin-top:26px}
.features{display:flex;gap:25px;margin-top:26px}
.feature{width:238px;height:264px;background:#fff;box-shadow:0 2px 12px rgba(0,0,0,.08);text-align:center;padding:40px 20px 0}
.icon-box{width:68px;height:68px;margin:0 auto;border-radius:4px;background:var(--green-soft);display:flex;align-items:center;justify-content:center}
.feature h3{font-size:18px;font-weight:500;color:var(--ink);margin-top:20px}
.feature p{font-size:13px;color:var(--muted);line-height:1.6;margin-top:10px}

/* courses */
.courses{background:var(--sand);margin-top:96px;height:742px;padding-top:88px}
.cards{display:flex;gap:25px;margin-top:36px}
.card{width:326px}
.card-media{position:relative;height:208px;border-radius:4px}
.tags{position:absolute;top:20px;left:20px;display:flex;gap:12px}
.tag{background:#fff;color:var(--green);font-size:12px;padding:3px 15px;border-radius:3px}
.price{position:absolute;right:15px;bottom:-10px;background:#fff;color:var(--green);font-size:13px;padding:3px 14px;border-radius:3px}
.card-body{padding:30px 17px 0}
.card h3{font-size:19px;font-weight:500;color:var(--ink);line-height:1.5}
.card p{font-size:14.5px;color:var(--muted);margin-top:12px;line-height:1.65}
.more{display:inline-block;color:var(--green);font-size:13px;margin-top:14px}

/* webinar */
.webinar{padding-top:92px;height:586px}
.webinar .wrap{height:495px}
.web-photo{position:absolute;right:0;top:37px;width:530px;height:417px;background:linear-gradient(135deg,#6b5a4c 0%,#3d3a38 40%,#1f2226 70%,#8a8c8f 100%);display:flex;align-items:center;justify-content:center}
.web-card{position:absolute;left:0;top:0;width:500px;height:495px;background:#fff;box-shadow:0 2px 14px rgba(0,0,0,.09);padding:48px 44px}
.web-card h2{font-size:40px;font-weight:500;color:var(--ink);line-height:1.2}
.web-card .underline{margin:12px 0 0}
.web-card p{font-size:15px;color:var(--muted);margin-top:22px;line-height:1.6}
.web-card p.strong{color:var(--ink)}
.web-card .btn{margin-top:26px}
.pbtn{width:46px;height:46px;border-radius:50%;background:#fff;display:flex;align-items:center;justify-content:center;box-shadow:0 0 0 10px rgba(255,255,255,.25)}

/* blog */
.blog{padding-top:20px;height:772px}
.posts{display:flex;gap:27px;margin-top:42px}
.post{width:501px}
.post-media{height:388px;border-radius:4px}
.meta{color:var(--green);font-size:13px;margin-top:24px}
.post h3{font-size:20px;font-weight:500;color:var(--ink);margin-top:8px}
.post p{font-size:15px;color:var(--muted);margin-top:6px;line-height:1.65}

/* one to one */
.oto{position:relative;height:370px;background:linear-gradient(90deg,#c7c2b8 0%,#b9b3a7 40%,#2a2f33 60%,#111 100%)}
.oto-text{position:absolute;left:636px;top:115px;color:#fff}
.oto-text h2{font-size:38px;font-weight:500}
.oto-text p{font-size:15px;width:430px;margin-top:18px;color:#e4e4e4}
.oto-text .more{color:#fff}

/* footer */
.footer{padding-top:102px}
.foot-top{display:flex;align-items:center;border-bottom:1px solid var(--line);padding-bottom:40px}
.follow{margin-left:auto;display:flex;align-items:center;gap:18px;font-size:14px;color:var(--ink)}
.social{width:16px;height:16px;border-radius:50%;background:#888}
.cols{display:flex;padding-top:40px;height:260px}
.col h4{font-size:18px;font-weight:500;color:var(--ink);margin-bottom:24px}
.col p,.col li{font-size:14px;color:var(--text);line-height:1.75}
.col ul{list-style:none}
.col li{margin-bottom:20px}
.about{width:455px}
.about p{width:320px}
.links{width:162px}
.services{width:194px}
.contact p{margin-bottom:14px}
.copy{border-top:1px solid var(--line);text-align:center;font-size:14px;color:var(--ink);padding-top:24px}
</style>
</head>
<body>

<header>
  <div class="topbar">
    <div class="wrap">
      <div class="item">
        <svg width="14" height="14" viewBox="0 0 24 24" fill="#22b24c"><path d="M6.6 10.8a15.1 15.1 0 0 0 6.6 6.6l2.2-2.2a1 1 0 0 1 1-.25 11.4 11.4 0 0 0 3.6.57 1 1 0 0 1 1 1V20a1 1 0 0 1-1 1A17 17 0 0 1 3 4a1 1 0 0 1 1-1h3.5a1 1 0 0 1 1 1c0 1.25.2 2.45.57 3.57a1 1 0 0 1-.25 1z"/></svg>
        Call: +45 3148 5290
      </div>
      <div class="sep"></div>
      <div class="item">
        <svg width="16" height="12" viewBox="0 0 16 12" fill="#22b24c"><path d="M0 0h16v12H0z"/><path d="M0 0l8 6 8-6" stroke="#111417" stroke-width="1.4" fill="none"/></svg>
        Email: hello@deskwizard.dk
      </div>
      <div class="right">
        <a>Sign In</a><span class="sep" style="margin:0"></span><a>Register</a>
        <a class="apply">Apply Now <svg class="arrow" viewBox="0 0 14 8"><path d="M0 4h12M9 1l3 3-3 3" stroke="#fff" fill="none"/></svg></a>
      </div>
    </div>
  </div>
  <nav class="nav">
    <div class="wrap">
      <div class="logo">deskwizard</div>
      <div class="menu">
        <a>Courses</a><a>Webinar</a><a>One to one</a><a>Questions</a><a>Blog</a><a>About</a><a>Contact</a>
        <span class="bar"></span>
        <svg width="18" height="18" viewBox="0 0 20 20"><circle cx="8.5" cy="8.5" r="6.5" stroke="#111" stroke-width="1.6" fill="none"/><path d="M13.5 13.5l5 5" stroke="#111" stroke-width="1.6"/></svg>
      </div>
    </div>
  </nav>
</header>

<main>
  <section class="hero">
    <div class="hero-photo" role="img" aria-label="Hands typing on a laptop resting on a white bed"></div>
    <div class="wrap">
      <div class="eyebrow">Welcome to DeskWizard</div>
      <h1>Strengthen your IT skills with "just-in-time" learning</h1>
      <p>I offer online courses and webinars with a clear focus, or what about online "One to One" teaching</p>
      <div class="actions">
        <a class="btn">Get Started <svg class="arrow" viewBox="0 0 14 8"><path d="M0 4h12M9 1l3 3-3 3" stroke="#fff" fill="none"/></svg></a>
        <a class="watch"><span class="play"><svg width="10" height="12" viewBox="0 0 10 12"><path d="M0 0l10 6-10 6z" fill="#fff"/></svg></span>Watch Video</a>
      </div>
    </div>
    <svg class="wave" viewBox="0 0 1200 70" preserveAspectRatio="none">
      <path d="M0 58 C300 70 500 30 800 42 S1100 48 1200 40 V70 H0Z" fill="#fff"/>
      <path d="M0 58 C300 70 500 30 800 42 S1100 48 1200 40" stroke="#22b24c" stroke-width="5" fill="none"/>
    </svg>
  </section>

  <section class="why" style="height:auto">
    <div class="wrap">
      <div class="head">
        <h2>Why <span>DeskWizard?</span></h2>
        <svg class="underline" viewBox="0 0 66 10"><path d="M3 7 Q33 0 63 7" stroke="#22b24c" stroke-width="4" fill="none" stroke-linecap="round"/></svg>
      </div>
      <p class="lead">I have been teaching a lot of happy students since 1995.</p>
      <div class="features">
        <div class="feature">
          <div class="icon-box"><svg width="34" height="34" viewBox="0 0 34 34" fill="none" stroke="#22b24c" stroke-width="1.5"><circle cx="20" cy="10" r="6"/><path d="M4 26h6l8 3 12-7-2-2-9 4M10 22h8"/></svg></div>
          <h3>Good Economy</h3>
          <p>The price of an online course is lower than a physical course</p>
        </div>
        <div class="feature">
          <div class="icon-box"><svg width="34" height="34" viewBox="0 0 34 34" fill="none" stroke="#22b24c" stroke-width="1.5"><path d="M17 6a8 8 0 0 0-5 14v4h10v-4a8 8 0 0 0-5-14zM13 28h8"/></svg></div>
          <h3>Why Wait</h3>
          <p>Strengthen your skills on an online course now</p>
        </div>
        <div class="feature">
          <div class="icon-box"><svg width="38" height="30" viewBox="0 0 38 30" fill="none" stroke="#22b24c" stroke-width="1.5"><path d="M4 6h20v14H4zM24 10h6l5 5v5H24z"/><circle cx="10" cy="22" r="3"/><circle cx="29" cy="22" r="3"/></svg></div>
          <h3>No Travel Time</h3>
          <p>You avoid wasted time and decide for yourself what to have for lunch</p>
        </div>
        <div class="feature">
          <div class="icon-box"><svg width="30" height="30" viewBox="0 0 30 30" fill="none" stroke="#22b24c" stroke-width="1.5"><path d="M10 5h15v15H10zM5 10v15h15"/></svg></div>
          <h3>Designed in a Browser</h3>
          <p>Designing in a browser allows rapid development and saves cost.</p>
        </div>
      </div>
    </div>
  </section>

  <section class="courses">
    <div class="wrap">
      <div class="head">
        <h2>Online Courses</h2>
        <svg class="underline" viewBox="0 0 66 10"><path d="M3 7 Q33 0 63 7" stroke="#22b24c" stroke-width="4" fill="none" stroke-linecap="round"/></svg>
      </div>
      <div class="cards">
        <article class="card">
          <div class="card-media" role="img" aria-label="Reporting software logo on a tablet with a yellow arrow" style="background:linear-gradient(135deg,#3b3a36,#c8b737 55%,#7a7a72)">
            <div class="tags"><span class="tag">LUMO</span></div>
            <span class="price">199 kr</span>
          </div>
          <div class="card-body">
            <h3>Lumo Reports in one hour</h3>
            <p>Is it possible to learn Lumo Reports in just one hour? Probably not, but I can give you an introduction.</p>
            <a class="more">Learn More <svg class="arrow" viewBox="0 0 14 8"><path d="M0 4h12M9 1l3 3-3 3" stroke="#22b24c" fill="none"/></svg></a>
          </div>
        </article>
        <article class="card">
          <div class="card-media" role="img" aria-label="Laptop showing a programming language logo" style="background:linear-gradient(160deg,#f2f2f2,#d9dde0 60%,#9aa3a8)">
            <div class="tags"><span class="tag">SCRIPTLY</span><span class="tag">SHEETLY</span></div>
            <span class="price">499 kr</span>
          </div>
          <div class="card-body">
            <h3>Scriptly for Sheetly users</h3>
            <p>How do you as Sheetly users get started using Scriptly</p>
            <a class="more">Learn More <svg class="arrow" viewBox="0 0 14 8"><path d="M0 4h12M9 1l3 3-3 3" stroke="#22b24c" fill="none"/></svg></a>
          </div>
        </article>
        <article class="card">
          <div class="card-media" role="img" aria-label="Programming website on a blue screen" style="background:linear-gradient(135deg,#1d2f7a,#3257b8 55%,#c9d3e6)">
            <div class="tags"><span class="tag">SCRIPTLY</span></div>
            <span class="price">499 kr</span>
          </div>
          <div class="card-body">
            <h3>Stato Introduction</h3>
            <p>Introduction to Stato programming.</p>
            <a class="more">Learn More <svg class="arrow" viewBox="0 0 14 8"><path d="M0 4h12M9 1l3 3-3 3" stroke="#22b24c" fill="none"/></svg></a>
          </div>
        </article>
      </div>
    </div>
  </section>

  <section class="webinar">
    <div class="wrap">
      <div class="web-photo" role="img" aria-label="Person working at a desktop computer in a dim room">
        <span class="pbtn"><svg width="14" height="16" viewBox="0 0 10 12"><path d="M0 0l10 6-10 6z" fill="#22b24c"/></svg></span>
      </div>
      <div class="web-card">
        <h2>Webinar</h2>
        <svg class="underline" viewBox="0 0 66 10"><path d="M3 7 Q33 0 63 7" stroke="#22b24c" stroke-width="4" fill="none" stroke-linecap="round"/></svg>
        <p class="strong">It is not only on the price that webinars beat traditional courses!</p>
        <p>You get the same high quality in a webinar as in a traditional course, even with the advantage that you can watch them again and again.</p>
        <p>Best of all, you do not have to move to gain new knowledge</p>
        <a class="btn">Webinar <svg class="arrow" viewBox="0 0 14 8"><path d="M0 4h12M9 1l3 3-3 3" stroke="#fff" fill="none"/></svg></a>
      </div>
    </div>
  </section>

  <section class="blog">
    <div class="wrap">
      <div class="head">
        <h2>Latest blog posts</h2>
        <svg class="underline" viewBox="0 0 66 10"><path d="M3 7 Q33 0 63 7" stroke="#22b24c" stroke-width="4" fill="none" stroke-linecap="round"/></svg>
      </div>
      <div class="posts">
        <article class="post">
          <div class="post-media" role="img" aria-label="Spreadsheet with a running total column" style="background:linear-gradient(180deg,#f1f1f1 0%,#f1f1f1 6%,#3f6bc4 6%,#3f6bc4 34%,#dfe8f5 34%)"></div>
          <div class="meta">July 04, 2022 • Sheetly</div>
          <h3>Current sum</h3>
          <p>Creation of current totals</p>
          <a class="more">Read the article <svg class="arrow" viewBox="0 0 14 8"><path d="M0 4h12M9 1l3 3-3 3" stroke="#22b24c" fill="none"/></svg></a>
        </article>
        <article class="post">
          <div class="post-media" role="img" aria-label="Laptop showing a spreadsheet next to a coffee cup and phone" style="background:linear-gradient(135deg,#e8e6e2,#cfcac2 40%,#7f8285 75%,#d8d6d2)"></div>
          <div class="meta">July 17, 2022 • Sheetly</div>
          <h3>Brug Lumo Reports data i Sheetly</h3>
          <p>Lumo Reports is a great program for analyzing, viewing and sharing your report - But what if you want to analyze further on data in Sheetly?</p>
          <a class="more">Read the article <svg class="arrow" viewBox="0 0 14 8"><path d="M0 4h12M9 1l3 3-3 3" stroke="#22b24c" fill="none"/></svg></a>
        </article>
      </div>
    </div>
  </section>

  <section class="oto" role="img" aria-label="Teacher working on a laptop in a classroom">
    <div class="oto-text">
      <h2>One to One</h2>
      <p>Targeted teaching at just the right time will make you better and faster for your assignments</p>
      <a class="more">Learn More <svg class="arrow" viewBox="0 0 14 8"><path d="M0 4h12M9 1l3 3-3 3" stroke="#fff" fill="none"/></svg></a>
    </div>
  </section>
</main>

<footer class="footer">
  <div class="wrap">
    <div class="foot-top">
      <div class="logo">deskwizard</div>
      <div class="follow">Follow Us: <span class="social"></span><span class="social"></span><span class="social"></span></div>
    </div>
    <div class="cols">
      <div class="col about">
        <h4>About Us</h4>
        <p>Since 1995, I have taught companies and for course providers. Over the years, it has become a lot of satisfied students. I also teach at Nordvik Tech and Havborg Academy, where the future IT employees are responsible for the shots.</p>
      </div>
      <div class="col links">
        <h4>Links</h4>
        <ul><li>Blog</li><li>About</li><li>Contact</li><li>Terms</li></ul>
      </div>
      <div class="col services">
        <h4>Services</h4>
        <ul><li>Online Courses</li><li>Webinar</li><li>One to one</li><li>Questions</li></ul>
      </div>
      <div class="col contact">
        <h4>Contact</h4>
        <p>If you have any questions or anything else please contact me</p>
        <p>Lindevej 14, 3060 Espergærde</p>
        <p>Call: +45 3148 5290</p>
        <p>Email: hello@deskwizard.dk</p>
      </div>
    </div>
    <div class="copy">Copyright © 2022</div>
  </div>
</footer>

</body>
</html>
```